Brochure Design Project for Brockwin and Daughters Lumber

We are after an executive high-end trifold brochure to be sent to new customers. Please refer to document attached ('brochure notes') for the details.

Target Market(s)

Renovators, Wives, Architects, Builders

Requirements
Must have
• Back of brochure must have a map and contact details.

Must relate to the feel of our website ... brockwinanddaughterslumber.net

Nice to have
• A unique design - something unlike regular brochures.

Developed using Adobe Photoshop or InDesign

```html
<!DOCTYPE html>
<html lang="en">
<head>
<meta charset="utf-8">
<title>Brockwin and Daughters Lumber – Trifold Brochure</title>
<link href="https://fonts.googleapis.com/css2?family=Questrial&family=PT+Sans+Narrow&display=swap" rel="stylesheet">
<style>
  :root{
    --lime:#8fcb2b;
    --lime-soft:#b5dc62;
    --paper:#eef2cf;
    --ink:#3b3b2e;
    --white:#ffffff;
    --stage:#e4e0d6;
    --fold:rgba(0,0,0,0.10);
  }
  *{box-sizing:border-box;margin:0;padding:0}
  html,body{width:1200px;height:1000px;overflow:hidden}
  body{background:var(--stage);font-family:"Questrial",sans-serif;color:var(--ink);position:relative}

  .spread{position:absolute;display:flex;height:470px;box-shadow:0 4px 14px rgba(0,0,0,.18)}
  .spread--outside{left:40px;top:18px}
  .spread--inside{left:440px;top:512px}
  .panel{position:relative;width:240px;height:470px;background:var(--paper);overflow:hidden}
  .panel + .panel{border-left:1px solid var(--fold)}

  /* ---------- outside: offer panel ---------- */
  .offer-card{position:absolute;inset:14px 16px 14px 14px;background:var(--lime);border-radius:4px;padding:10px}
  .offer-card__frame{height:100%;border:1.5px solid rgba(255,255,255,.75);border-radius:16px;padding:96px 14px 0;color:var(--white)}
  .offer-card__title{font-size:21px;letter-spacing:1px;text-align:center;margin-bottom:12px;font-weight:400}
  .offer-card__list{list-style:none;font-size:10.5px;line-height:1.32}
  .offer-card__list li{margin-bottom:11px;text-align:justify}

  /* ---------- outside: contact panel ---------- */
  .map{position:absolute;left:18px;top:18px;width:204px;height:204px;background:linear-gradient(135deg,#f2f2f2,#dcdcdc 60%,#e8efe0);box-shadow:0 1px 4px rgba(0,0,0,.2)}
  .contact{position:absolute;left:0;right:0;top:290px;text-align:center;font-family:"PT Sans Narrow",sans-serif;font-size:14px;line-height:1.3;color:var(--ink);font-style:normal}
  .contact__web{font-size:15px;letter-spacing:.3px;margin-top:2px}
  .brand{display:flex;align-items:center;justify-content:center;gap:7px;font-family:"Questrial",sans-serif;color:var(--lime)}
  .brand__dot{width:14px;height:14px;border-radius:50%;background:var(--lime);flex:none}
  .brand--back{position:absolute;left:0;right:0;top:418px;font-size:13px}

  /* ---------- outside: cover ---------- */
  .cover__stripe{position:absolute;right:0;top:0;width:20px;height:100%;background:var(--lime)}
  .cover__title{position:absolute;left:18px;top:40px;color:var(--lime);font-weight:400;line-height:1}
  .cover__title-top{display:block;font-size:19px}
  .cover__title-main{display:block;font-size:26px;margin:2px 0 0 62px;color:var(--lime-soft);letter-spacing:.5px}
  .cover__photo{position:absolute;left:20px;top:108px;width:184px;height:198px;background:linear-gradient(170deg,#3d6fa8 0%,#2d4f6d 30%,#4e7a3e 50%,#7a4a35 75%,#5d3a2b 100%);box-shadow:0 2px 5px rgba(0,0,0,.25)}
  .brand--cover{position:absolute;left:0;right:20px;top:360px;flex-direction:column;gap:6px;font-size:14px;text-align:center}
  .brand--cover .brand__dot{width:48px;height:48px}

  /* ---------- inside ---------- */
  .inside-stripe{position:absolute;left:0;top:0;width:16px;height:100%;background:var(--lime)}
  .heading{font-size:11.5px;font-weight:400;letter-spacing:.6px;text-align:center;text-transform:uppercase;color:var(--ink)}
  .copy{font-size:10.3px;line-height:1.3;text-align:justify}
  .photo{box-shadow:0 3px 6px rgba(0,0,0,.3);border-radius:0 62px 0 62px}

  .panel--composite{padding:34px 16px 0 30px}
  .panel--composite .heading{margin-bottom:12px}
  .composite__note{font-size:10.8px;line-height:1.3;margin-top:10px;font-weight:700;color:#2e2e24}
  .photo--fence{width:196px;height:150px;margin-top:14px;background:linear-gradient(180deg,#3f88d8 0%,#86b8e6 30%,#9c8270 45%,#c9c3b2 55%,#4f8c2f 75%,#3d7a22 100%)}
  .panel--composite .heading--fence{margin-top:14px;margin-bottom:8px}
  .composite__cta{font-size:10.3px;font-style:italic;text-align:center;margin-top:8px}

  .panel--tonka{padding:22px 14px 0 14px}
  .panel--tonka .heading{margin-bottom:10px}
  .tonka__sub{font-size:10.3px;text-transform:uppercase;margin:12px 0 7px}
  .tonka__list{list-style:none;font-size:10.3px;line-height:1.3}
  .tonka__list li{padding-left:8px;text-indent:-8px}
  .tonka__list li::before{content:"* "}
  .photo--deck{width:204px;height:118px;margin-top:8px;background:linear-gradient(200deg,#e8e0cf 0%,#b4693a 28%,#8d4422 55%,#6a3018 100%)}

  .panel--flooring{padding:22px 16px 0 16px}
  .photo--kitchen{width:206px;height:196px;background:linear-gradient(180deg,#2c2420 0%,#6e6a62 30%,#e7e6e2 48%,#a0552a 70%,#7a3b1c 100%)}
  .panel--flooring .heading{margin:30px 0 12px}
  .panel--flooring .copy + .copy{margin-top:12px}
</style>
</head>
<body>

<section class="spread spread--outside">
  <div class="panel panel--offer">
    <div class="offer-card">
      <div class="offer-card__frame">
        <h2 class="offer-card__title">WANT CASH?</h2>
        <ul class="offer-card__list">
          <li>* Become a renovation star! If you allow us to take photos, video or leave a sign, we will reward you with $50 cash for every order taken from interest in your home improvement.</li>
          <li>* We can come to you for free measure and quote.</li>
          <li>* Design advise</li>
          <li>* Can organize full installation.</li>
        </ul>
      </div>
    </div>
  </div>

  <div class="panel panel--contact">
    <div class="map" role="img" aria-label="Street map showing the yard location and surrounding roads and parks"></div>
    <address class="contact">
      <div>27 Wattlebark Lane Kinross</div>
      <div>Harrowfield, Eastmere</div>
      <div>Australia 4872</div>
      <div>Phone +61 7 3190 4826</div>
      <div class="contact__web">www.brockwinanddaughterslumber.net</div>
    </address>
    <div class="brand brand--back"><span class="brand__dot"></span><span>Brockwin and Daughters Lumber</span></div>
  </div>

  <div class="panel panel--cover">
    <div class="cover__stripe"></div>
    <h1 class="cover__title">
      <span class="cover__title-top">Building Better</span>
      <span class="cover__title-main">LIFESTYLE</span>
    </h1>
    <div class="cover__photo" role="img" aria-label="Photo of a waterfront timber deck with a boat jetty and palms"></div>
    <div class="brand brand--cover"><span class="brand__dot"></span><span>Brockwin and Daughters Lumber</span></div>
  </div>
</section>

<section class="spread spread--inside">
  <div class="panel panel--composite">
    <div class="inside-stripe"></div>
    <h3 class="heading">Composite Timber</h3>
    <p class="copy">Timber decks and screening are very popular but require constant maintenance. This timber-like product gives the look of timber, but with minimal upkeep.</p>
    <p class="composite__note">• The 'greenest of green' ... This timber-like product will give you the look you're after, without needing to oil .... EVER!</p>
    <div class="photo photo--fence" role="img" aria-label="Photo of a slatted designer fence above a green lawn"></div>
    <h3 class="heading heading--fence">Feature Fencing</h3>
    <p class="copy">We are able to supply you with designer fencing fully installed for much less than you think. Endless combinations available.</p>
    <p class="composite__cta">Call for an obligation-free quote today.</p>
  </div>

  <div class="panel panel--tonka">
    <h3 class="heading">Tonka Timber</h3>
    <p class="copy">The products include decking, flooring, structural timber and step treads.<br>Tonka flooring is warm reddish-brown or purplish-brown with lighter streaks and on exposure gradually becomes uniform light brown.<br>It doesn't bleed like merbau which is ideal around wet areas. Futher it carries independent 'Forest Pure' certification that it is sourced fromm 100% legal and well-managed forests.</p>
    <p class="tonka__sub">Benefits of the Tonka Timber species:</p>
    <ul class="tonka__list">
      <li>Durability Class 1 – no need to treat with nasty chemicals</li>
      <li>Environmentally sustainable – fully certified</li>
      <li>Strong</li>
      <li>Beautiful</li>
      <li>Wide range of uses available – decking, step treads, posts, joists.</li>
    </ul>
    <div class="photo photo--deck" role="img" aria-label="Photo of a reddish-brown hardwood deck"></div>
  </div>

  <div class="panel panel--flooring">
    <div class="photo photo--kitchen" role="img" aria-label="Photo of a modern kitchen with polished timber floor"></div>
    <h3 class="heading">Traditional Timber and<br>Bamboo Flooring</h3>
    <p class="copy">Timber flooring is a natural, environmentally friendly option that can add real value to your home. We can simply supply to DIY er's or can organise install, sand and finishing.</p>
    <p class="copy">Bamboo flooring is becoming an increasingly popular choice for many homeowners, architects, builders and interior designers who are looking for an environmental alternative to timber flooring that is a stylish, hard wearing, pre-finished flooring system.</p>
  </div>
</section>

</body>
</html>
```